Larkwell Bend responsive web design

We need a responsive, bootstrap compatible (but design only - PSD files) website design for a fly fishing shop and guide service.

Design should be very clean. Home Page design + interior page design please.

Possible Home Page Content:
Slide Show
Highlight Three Features: Guided Trips, Fly Shop, Missouri River
About

Thank you and good luck!

Industry/Entity Type

Shop

Requirements
Must have
• This will be used on Bootstrap CMS so needs 12 column bootstrap measurements.

DESIGN ONLY NEEDED (clean PSD files), no programming required.
Need a Home Page layout and secondary page layout

Must show use of the following:
H1 - H5 font uses
link color
Dropdown for navigation bar
Button example
Should not have
• No cutout images, this will be part of CMS and client needs to be able to update most content without knowing photoshop.

```html
<!DOCTYPE html>
<html lang="en">
<head>
<meta charset="utf-8">
<title>Larkwell Bend — Fly Fishing Shop &amp; Guide Service</title>
<link href="https://fonts.googleapis.com/css2?family=Open+Sans:ital,wght@0,400;0,600;0,700;1,400&display=swap" rel="stylesheet">
<style>
:root{
  --blue:#1a7fc1;
  --blue-dark:#176ea8;
  --text:#4a4a4a;
  --muted:#8a8a8a;
  --rule:#d9d9d9;
  --band:#f1f1f1;
  --white:#ffffff;
  --footer:#1e1f21;
  --field:#e6e6e6;
}
*{box-sizing:border-box;margin:0;padding:0}
html,body{width:1200px;height:2281px;overflow:hidden}
body{font-family:"Open Sans",Arial,sans-serif;color:var(--text);background:var(--white);font-size:14px;line-height:20px;position:relative}
a{color:var(--blue);text-decoration:none}
.wrap{width:1100px;margin:0 auto;position:relative}

/* header */
.site-header{height:100px;background:var(--white)}
.site-header .wrap{height:100px;display:flex;align-items:center;justify-content:space-between}
.brand{display:flex;align-items:center;gap:10px;font-weight:700;font-size:22px;color:var(--blue-dark)}
.brand-mark{width:22px;height:22px;background:var(--blue-dark);border-radius:50%}
.main-nav{display:flex;height:100px}
.main-nav a{display:flex;align-items:center;padding:0 22px;font-size:15px;color:#333;text-transform:uppercase;height:100px}
.main-nav a.active{background:#f0f0f0;color:var(--blue);border-top:3px solid var(--blue)}

/* hero */
.hero{position:relative;height:512px;background:linear-gradient(180deg,#4e7a3a 0%,#6f9b4f 40%,#8fb4a6 70%,#5d7f6a 100%)}
.hero-caption{position:absolute;top:178px;left:0;right:0;text-align:center;color:var(--white)}
.hero-caption h1{font-size:37px;font-weight:700;line-height:48px;text-shadow:0 2px 4px rgba(0,0,0,.4)}
.hero-caption p{font-size:15px;line-height:21px;margin-top:6px;text-shadow:0 1px 3px rgba(0,0,0,.5)}
.btn-outline{display:inline-block;margin-top:14px;border:2px solid var(--white);border-radius:6px;padding:6px 24px;color:var(--white);font-weight:600;font-size:15px;background:rgba(0,0,0,.25)}
.hero-arrow{position:absolute;top:338px;width:36px;height:36px;border-radius:50%;background:var(--blue);display:flex;align-items:center;justify-content:center}
.hero-arrow.prev{left:52px}
.hero-arrow.next{right:56px}

/* features */
.section-title{font-size:19px;font-weight:700;color:var(--blue);text-transform:uppercase;padding-bottom:10px;border-bottom:1px solid var(--rule);position:relative;margin-top:60px}
.section-title::after{content:"";position:absolute;left:0;bottom:-2px;width:160px;height:3px;background:var(--blue)}
.features{display:flex;gap:26px;margin-top:28px}
.feature{width:349px}
.feature-photo{height:172px}
.feature h3{font-size:17px;font-weight:700;color:var(--blue);margin-top:20px}
.feature p{font-size:14px;line-height:20px;margin-top:10px}

/* about band */
.band{background:var(--band);margin-top:46px;height:351px}
.band .wrap{display:flex;gap:38px;padding-top:50px}
.about{width:712px}
.news{width:350px}
h2.block-title{font-size:18px;font-weight:700;color:var(--blue-dark);margin-bottom:10px}
.about p{font-size:14px;line-height:20px;margin-bottom:22px}
.news-item{padding-bottom:12px;margin-bottom:14px;border-bottom:1px solid var(--rule)}
.news-item:last-child{border:0}
.news-item h4{font-size:13px;font-weight:700;color:#333}
.news-item time{display:block;font-size:10px;color:var(--blue);line-height:16px}
.news-item p{font-size:14px;line-height:20px}

/* gallery & testimonials */
.showcase .wrap{display:flex;gap:28px;padding-top:62px}
.gallery{width:723px}
.gallery-grid{display:grid;grid-template-columns:repeat(3,241px);grid-template-rows:repeat(2,168px);margin-top:4px}
.tile{position:relative}
.tile.highlight{background:rgba(40,170,220,.85);display:flex;flex-direction:column;align-items:center;justify-content:center;color:var(--white);font-size:16px;gap:10px}
.testimonials{width:349px}
.quote{font-style:italic;font-size:14px;line-height:21px;color:var(--muted);position:relative;padding-left:20px}
.quote .mark{position:absolute;left:0;top:-4px;font-size:26px;color:var(--blue);font-style:normal;font-weight:700}
.quote .mark.end{left:auto;right:0;top:auto;bottom:-16px}
.client{margin-top:22px;display:flex;justify-content:space-between;align-items:flex-end}
.client strong{display:block;color:var(--blue);font-size:15px}
.client span{font-size:10px;color:var(--muted);font-style:italic}
.pager{display:flex;gap:4px}
.pager i{width:20px;height:20px;border-radius:4px;background:#ddd;display:flex;align-items:center;justify-content:center}
.pager i.on{background:var(--blue)}

/* footer */
.site-footer{position:absolute;left:0;top:1900px;width:1200px;height:381px;background:linear-gradient(180deg,#262729 0%,#1b1c1e 100%);color:#e8e8e8}
.site-footer .cols{display:flex;gap:25px;padding-top:55px}
.site-footer .col{width:350px}
.site-footer h5{font-size:19px;font-weight:400;color:var(--blue);text-transform:uppercase;display:flex;align-items:center;gap:14px;margin-bottom:24px}
.site-footer p{font-size:14px;line-height:21px}
.contact-lines{margin-top:22px}
.contact-lines b{color:var(--white)}
.contact-lines .phone{color:var(--blue)}
.field{display:block;width:350px;height:32px;border-radius:6px;background:var(--field);border:0;font:13px "Open Sans",Arial,sans-serif;color:#555;padding:0 14px;margin-bottom:12px}
textarea.field{height:70px;padding-top:6px;resize:none}
.btn-ghost{display:inline-block;border:1px solid var(--white);border-radius:6px;padding:4px 16px;color:var(--white);font-size:13px;text-transform:uppercase}
.connect{font-size:18px;text-transform:uppercase;margin:30px 0 10px}
.social{display:flex;gap:10px}
.social i{width:32px;height:32px;border:2px solid #e8e8e8;border-radius:50%}
.footer-bottom{position:absolute;left:0;right:0;bottom:0;height:57px;border-top:1px solid #3a3b3d;text-align:center;font-size:12px;line-height:57px;color:#ddd}
</style>
</head>
<body>

<header class="site-header">
  <div class="wrap">
    <div class="brand"><span class="brand-mark"></span>Larkwell Bend</div>
    <nav class="main-nav">
      <a class="active" href="#">Home</a><a href="#">Trips</a><a href="#">Rivers</a><a href="#">Guides</a><a href="#">Rates</a><a href="#">Equipment</a><a href="#">Packages</a><a href="#">Lodging</a>
    </nav>
  </div>
</header>

<section class="hero" role="img" aria-label="Angler casting a fly rod in a clear river lined with green forest">
  <div class="hero-caption">
    <h1>Welcome to the Larkwell Bend web site!</h1>
    <p>Lorem ipsum dolor sit amet, consectetur adipisicing elit,<br>sed do eiusmod tempor incididunt ut labore et dolore magna.</p>
    <a class="btn-outline" href="#">Read More</a>
  </div>
  <span class="hero-arrow prev"><svg width="14" height="14" viewBox="0 0 14 14"><path d="M9 2 4 7l5 5" fill="none" stroke="#fff" stroke-width="2.5"/></svg></span>
  <span class="hero-arrow next"><svg width="14" height="14" viewBox="0 0 14 14"><path d="M5 2l5 5-5 5" fill="none" stroke="#fff" stroke-width="2.5"/></svg></span>
</section>

<main>
  <div class="wrap">
    <h2 class="section-title">Features</h2>
    <div class="features">
      <article class="feature">
        <div class="feature-photo" role="img" aria-label="Rocky hillside above a calm river" style="background:linear-gradient(180deg,#9fb8d2 0%,#b7a98a 50%,#4f6f87 100%)"></div>
        <h3>Guided Trips</h3>
        <p>Lorem ipsum dolor sit amet, consectetur adipisicing elit, sed do eiusmod tempor incididunt ut labore et dolore magna <a href="#">Read More...</a></p>
      </article>
      <article class="feature">
        <div class="feature-photo" role="img" aria-label="Interior of the fly shop with shelves and tables" style="background:linear-gradient(180deg,#b48a4f 0%,#c9a56c 50%,#8a6a45 100%)"></div>
        <h3>Fly Shop</h3>
        <p>Lorem ipsum dolor sit amet, consectetur adipisicing elit, sed do eiusmod tempor incididunt ut labore et dolore magna <a href="#">Read More...</a></p>
      </article>
      <article class="feature">
        <div class="feature-photo" role="img" aria-label="Two anglers on a boat on the river" style="background:linear-gradient(180deg,#a38a6a 0%,#8a9aa2 55%,#3f6f96 100%)"></div>
        <h3>Missouri River</h3>
        <p>Lorem ipsum dolor sit amet, consectetur adipisicing elit, sed do eiusmod tempor incididunt ut labore et dolore magna <a href="#">Read More...</a></p>
      </article>
    </div>
  </div>

  <section class="band">
    <div class="wrap">
      <div class="about">
        <h2 class="block-title">About Larkwell Bend</h2>
        <p>Lorem ipsum dolor sit amet, consectetur adipisicing elit, sed do eiusmod tempor incididunt ut labore et dolore magna Lorem ipsum dolor sit amet, consectetur adipisicing elit, sed do eiusmod tempor incididunt ut labore et dolore magna Lorem ipsum dolor sit amet, consectetur adipisicing elit, sed do eiusmod tempor incididunt ut labore et dolore magna Lorem ipsum dolor sit amet, consectetur adipisicing elit, sed do eiusmod tempor incididunt ut labore et dolore magna.</p>
        <p>Lorem ipsum dolor sit amet, consectetur adipisicing elit, sed do eiusmod tempor incididunt ut labore et dolore magna Lorem ipsum dolor sit amet, consectetur adipisicing elit, sed do eiusmod tempor incididunt ut labore et dolore magna Lorem ipsum abore et dolore magna Lorem ipsum dolor sit aincididunt ut labore et dolore magna <a href="#">Read More...</a></p>
      </div>
      <aside class="news">
        <h2 class="block-title">Latest News</h2>
        <div class="news-item">
          <h4>Lorem ipsum dolor sit amet</h4>
          <time>April 15th, 2014</time>
          <p>Lorem ipsum dolor sit amet, consectetur adipisicing elit, sed do eiusmod tempor labo <a href="#">Read More...</a></p>
        </div>
        <div class="news-item">
          <h4>Lorem ipsum dolor sit amet</h4>
          <time>April 15th, 2014</time>
          <p>Lorem ipsum dolor sit amet, consectetur adipisicing elit, sed do eiusmod tempor labo <a href="#">Read More...</a></p>
        </div>
      </aside>
    </div>
  </section>

  <section class="showcase">
    <div class="wrap">
      <div class="gallery">
        <h2 class="block-title">Our Gallery</h2>
        <div class="gallery-grid">
          <div class="tile" role="img" aria-label="Fly shop building with a drift boat outside" style="background:linear-gradient(180deg,#d7dde2,#8b7a62)"></div>
          <div class="tile highlight" role="img" aria-label="Fly shop gallery image">
            Fly Shop
            <svg width="70" height="50" viewBox="0 0 70 50"><rect x="1" y="1" width="68" height="48" fill="none" stroke="#fff" stroke-width="2" stroke-dasharray="5 4"/><path d="M17 25q18-16 36 0q-18 16-36 0z" fill="none" stroke="#fff" stroke-width="2.5"/><circle cx="35" cy="25" r="5" fill="#fff"/></svg>
          </div>
          <div class="tile" role="img" aria-label="River at sunset" style="background:linear-gradient(180deg,#9db3c8,#c8a77d 55%,#4e6a85)"></div>
          <div class="tile" role="img" aria-label="Two anglers on the water" style="background:linear-gradient(180deg,#a7936f,#5f7f97)"></div>
          <div class="tile" role="img" aria-label="Rocky hills along the river" style="background:linear-gradient(180deg,#a9bfd5,#9e8e70 50%,#3d6788)"></div>
          <div class="tile" role="img" aria-label="Shop interior with display tables" style="background:linear-gradient(180deg,#9a8a6c,#bfa070)"></div>
        </div>
      </div>
      <aside class="testimonials">
        <h2 class="block-title">What Our Client's Say</h2>
        <blockquote class="quote">
          <span class="mark">&ldquo;</span>
          Lorem ipsum dolor sit amet, consectetur adipisicing elit, sed do eiusmod tempor incididunt ut labore et dolore magnaLorem ipsum dolor sit amet, consectetur adipisicing elit, sed do eiusmod tempor incididunt ut labore et dolore magna Lorem ipsum dolor sit amet, consectetur adipisicing elit, sed do eiusmod tempor incididunt ut labore et dolore magnaLorem ipsum dolor sit amet, consectetur adipisicing elit, sed do eiusmod tempor incididunt ut labore et dolore magna
          <span class="mark end">&rdquo;</span>
        </blockquote>
        <div class="client">
          <div><strong>Catherine Doe</strong><span>Client, Helena</span></div>
          <div class="pager">
            <i><svg width="8" height="10" viewBox="0 0 8 10"><path d="M6 1 2 5l4 4" fill="none" stroke="#666" stroke-width="2"/></svg></i>
            <i class="on"><svg width="8" height="10" viewBox="0 0 8 10"><path d="M2 1l4 4-4 4" fill="none" stroke="#fff" stroke-width="2"/></svg></i>
          </div>
        </div>
      </aside>
    </div>
  </section>
</main>

<footer class="site-footer" role="img" aria-label="Dark river scene behind the footer">
  <div class="wrap cols">
    <div class="col">
      <h5><svg width="16" height="22" viewBox="0 0 16 22"><path d="M8 0a8 8 0 0 0-8 8c0 6 8 14 8 14s8-8 8-14a8 8 0 0 0-8-8z" fill="#fff"/><circle cx="8" cy="8" r="3" fill="#222"/></svg>Location</h5>
      <p>Lorem ipsum dolor sit amet consectetur elit, sed do eiusmod tempor incididunt ut, labore et dolore magna.</p>
      <p class="contact-lines"><b>P :</b> <span class="phone">+1 800 555 0142</span><br><b>E :</b> info@larkwellbend.com</p>
    </div>
    <div class="col">
      <h5><svg width="26" height="18" viewBox="0 0 26 18"><rect x="1" y="1" width="24" height="16" fill="none" stroke="#fff" stroke-width="2"/><path d="M1 1l12 9 12-9" fill="none" stroke="#fff" stroke-width="2"/></svg>Newsletter!</h5>
      <input class="field" value="Enter Your Email" readonly>
      <span class="btn-ghost">Subscribe</span>
      <div class="connect">Connect with us</div>
      <div class="social"><i></i><i></i><i></i><i></i><i></i></div>
    </div>
    <div class="col">
      <h5><svg width="26" height="18" viewBox="0 0 26 18"><rect x="1" y="1" width="24" height="16" fill="none" stroke="#fff" stroke-width="2"/><path d="M1 1l12 9 12-9" fill="none" stroke="#fff" stroke-width="2"/></svg>Contact Form</h5>
      <input class="field" value="Enter Your Name" readonly>
      <input class="field" value="Enter Your Email" readonly>
      <textarea class="field" readonly>Enter Your Message</textarea>
      <span class="btn-ghost">Send</span>
    </div>
  </div>
  <div class="footer-bottom">Copyright ©2014 Larkwell Bend Ltd. All Rights Reserved.</div>
</footer>

</body>
</html>
```